Upgrade 4 Images - Bid 1, then we can discuss the other 3

We have a four graphics that we use in various presentations and business proposals. We want to upgrade them to make them really pop and match the level of service we provide, without going overboard.

We're open to new ideas, but the general form and content should stay the same.

I'd like to have all four designed by the same person, but I'm assuming this bid will be for 1 of the four, and then the other three can be contracted as additions.

```html
<!DOCTYPE html>
<html lang="en">
<head>
<meta charset="utf-8">
<title>Service Levels</title>
<link rel="stylesheet" href="https://fonts.googleapis.com/css2?family=Jost:wght@500&family=Roboto+Condensed:wght@700&display=swap">
<style>
  :root {
    --adhoc: #48d90f;
    --specialist: #08b8f2;
    --factory: #ebcf00;
    --enterprise: #003591;
    --ink: #333333;
    --mark: #222222;
    --card: #ffffff;
    --page: #ffffff;
    --rule: #bdbdbd;
  }
  html, body { margin: 0; padding: 0; overflow: hidden; background: var(--page); }
  .canvas { position: relative; width: 1200px; height: 743px; overflow: hidden; background: var(--page); }

  .stage {
    position: absolute; width: 242px; height: 242px; border-radius: 50%;
    background: var(--card);
    box-shadow: 0 6px 26px rgba(0,0,0,0.12);
  }
  .stage-cap {
    position: absolute; left: 22px; top: 20px; width: 198px; height: 99px;
    border-radius: 99px 99px 0 0;
    display: flex; align-items: flex-end; justify-content: center;
  }
  .stage-title {
    font-family: "Roboto Condensed", sans-serif; font-weight: 700;
    color: #fff; font-size: 25px; letter-spacing: 0.3px;
    margin-bottom: 26px; line-height: 1;
  }
  .stage-list {
    position: absolute; left: 0; right: 0; margin: 0; padding: 0; list-style: none;
    font-family: "Jost", sans-serif; font-weight: 500; font-size: 16.5px;
    color: var(--ink); text-align: center; letter-spacing: 0.5px;
  }
  .stage-list li { height: 24.5px; line-height: 24.5px; }
  .pair { display: flex; justify-content: center; align-items: center; }
  .pair .sep { width: 1px; height: 28px; background: var(--rule); margin: 0 10px; }

  .adhoc { left: 37px; top: 252px; }
  .adhoc .stage-cap { background: var(--adhoc); top: 19px; }
  .adhoc .stage-list { top: 138px; }

  .specialist { left: 488px; top: 70px; }
  .specialist .stage-cap { background: var(--specialist); top: 18px; }
  .specialist .stage-title { margin-bottom: 29px; }
  .specialist .stage-list { top: 130px; }
  .specialist .stage-list li { height: 31px; line-height: 31px; }

  .factory { left: 488px; top: 431px; }
  .factory .stage-cap { background: var(--factory); top: 19px; }
  .factory .stage-title { margin-bottom: 28px; }
  .factory .stage-list { top: 129px; }
  .factory .stage-list li { height: 30px; line-height: 30px; }

  .enterprise { left: 915px; top: 252px; }
  .enterprise .stage-cap { background: var(--enterprise); top: 19px; }
  .enterprise .stage-list { top: 125px; }
  .enterprise .stage-list li { height: 23px; line-height: 23px; }

  .operator { position: absolute; }
  .arrow { left: 330px; top: 325px; }
  .plus { left: 576px; top: 344px; }
  .equals { left: 776px; top: 343px; }
</style>
</head>
<body>
<main class="canvas">

  <svg class="operator arrow" width="136" height="96" viewBox="0 0 136 96" aria-hidden="true">
    <path d="M6 48 H124 M84 8 L124 48 L84 88" fill="none" stroke="var(--mark)" stroke-width="11" stroke-linecap="round" stroke-linejoin="round"/>
  </svg>

  <svg class="operator plus" width="58" height="58" viewBox="0 0 58 58" aria-hidden="true">
    <circle cx="29" cy="29" r="29" fill="var(--mark)"/>
    <path d="M29 16 V42 M16 29 H42" stroke="#fff" stroke-width="5" stroke-linecap="round"/>
  </svg>

  <svg class="operator equals" width="72" height="44" viewBox="0 0 72 44" aria-hidden="true">
    <path d="M5 6 H67 M5 36 H67" stroke="var(--mark)" stroke-width="10" stroke-linecap="round"/>
  </svg>

  <section class="stage adhoc">
    <div class="stage-cap"><h2 class="stage-title">AD HOC</h2></div>
    <ul class="stage-list">
      <li>Easy to Use</li>
      <li>Reduced errors</li>
      <li>24 Hour Window</li>
      <li>Job Queue</li>
    </ul>
  </section>

  <section class="stage specialist">
    <div class="stage-cap"><h2 class="stage-title">SPECIALIST</h2></div>
    <ul class="stage-list">
      <li class="pair"><span>Workflow</span><span class="sep"></span><span>Architecture</span></li>
      <li>Search Strategy</li>
      <li>Case Reporting</li>
    </ul>
  </section>

  <section class="stage factory">
    <div class="stage-cap"><h2 class="stage-title">FACTORY</h2></div>
    <ul class="stage-list">
      <li>Case Onboarding</li>
      <li class="pair"><span>Roles</span><span class="sep"></span><span>Data Re-use</span></li>
      <li>Resource Mgt</li>
    </ul>
  </section>

  <section class="stage enterprise">
    <div class="stage-cap"><h2 class="stage-title">ENTERPRISE</h2></div>
    <ul class="stage-list">
      <li>Cross-case Analytics</li>
      <li>Data Lakes</li>
      <li>Matrixes Use</li>
      <li>Recurring Jobs</li>
    </ul>
  </section>

</main>
</body>
</html>
```